Harborlight Capital Estates business card

We are a real estate advisory and investment company. We are specialized in assisting high networth individuals to invest in real estate overseas. We deliver a very personalized service, anticipating all the potential challenges an investor can face, and making it easy and safe for them. We also co-invest with our clients, assuring them that each project will be looked after as it is our own, and at the same time giving them the extra booth on confidence to invest.

We need a business card design. The business card must have a very premium, high-end look, reflecting principles like "commitment", "trust" and "timeless (but contemporary)". We look for long term relationships with our clients, and we grow with their referrals. We are all about conquering the confidence of the clients by always delivering above the expectations performance.

Target Market(s)

High net worth individuals.

Industry/Entity Type

Real Estate

Contact Information for Business Card

Please consider places on the business card for:

Name
Function (bellow name in smaller size text)

Mobile phone
E-mail
Skype ID
WeChat ID

Adress (3 lines)

Also include the following locations references:
PORTUGAL * DUBAI * HONG KONG

Website: www.hcestates-example.com

Requirements
Must have
• Company Logo

```html
<!DOCTYPE html>
<html lang="en">
<head>
<meta charset="utf-8">
<title>Harborlight Capital Estates – Business Card</title>
<link href="https://fonts.googleapis.com/css2?family=Mulish:wght@300;400;800&display=swap" rel="stylesheet">
<style>
  :root {
    --canvas: #e9ebee;
    --card-dark: #050505;
    --card-light: #ffffff;
    --accent: #29a3e3;
    --accent-soft: #5bb9ec;
    --text-grey: #6d6f72;
  }
  * { margin: 0; padding: 0; box-sizing: border-box; }
  html, body { width: 1200px; height: 1200px; overflow: hidden; }
  body {
    background: var(--canvas);
    font-family: "Mulish", sans-serif;
    position: relative;
  }
  .card {
    position: absolute;
    left: 180px;
    width: 840px;
    height: 480px;
    overflow: hidden;
    box-shadow: 0 10px 30px rgba(0,0,0,.18);
  }
  .card--front { top: 70px; background: var(--card-dark); }
  .card--back { top: 650px; background: var(--card-light); }

  /* front */
  .front-brand {
    position: absolute;
    top: 180px;
    left: 0; right: 0;
    text-align: center;
    color: var(--accent);
    font-weight: 400;
    font-size: 40px;
    letter-spacing: 3px;
    text-transform: uppercase;
  }
  .front-band {
    position: absolute;
    right: 0;
    bottom: 60px;
    width: 380px;
    height: 56px;
    background: linear-gradient(90deg, var(--accent-soft), var(--accent));
    border-top-left-radius: 22px;
  }

  /* back */
  .back-brand {
    position: absolute;
    top: 150px;
    left: 50px;
    width: 330px;
    color: var(--accent);
    font-weight: 400;
    font-size: 30px;
    line-height: 1.3;
    letter-spacing: 2px;
    text-transform: uppercase;
  }
  .divider {
    position: absolute;
    left: 420px;
    top: 70px;
    width: 3px;
    height: 300px;
    background: var(--accent);
  }
  .contact {
    position: absolute;
    left: 455px;
    top: 70px;
  }
  .contact__name {
    color: var(--accent);
    font-size: 34px;
    letter-spacing: 1px;
    font-weight: 400;
  }
  .contact__name strong { font-weight: 800; }
  .contact__role {
    color: var(--text-grey);
    font-weight: 300;
    font-size: 20px;
    margin: 2px 0 18px;
  }
  .contact__list { list-style: none; }
  .contact__item {
    display: flex;
    align-items: center;
    gap: 14px;
    color: var(--text-grey);
    font-size: 19px;
    height: 38px;
  }
  .contact__icon {
    width: 28px; height: 28px;
    border-radius: 50%;
    background: var(--accent);
    flex: none;
    display: flex; align-items: center; justify-content: center;
  }
  .address-band {
    position: absolute;
    left: 0;
    bottom: 0;
    width: 420px;
    height: 70px;
    background: var(--accent);
    border-top-right-radius: 22px;
    color: #fff;
    font-size: 19px;
    display: flex;
    align-items: center;
    padding-left: 40px;
  }
</style>
</head>
<body>
  <section class="card card--front" aria-label="Card front">
    <div class="front-brand">Harborlight Capital Estates</div>
    <div class="front-band"></div>
  </section>

  <section class="card card--back" aria-label="Card back">
    <div class="back-brand">Harborlight Capital Estates</div>
    <div class="divider"></div>
    <div class="contact">
      <h1 class="contact__name"><strong>ELIAN</strong> MARSH</h1>
      <p class="contact__role">Your Position</p>
      <ul class="contact__list">
        <li class="contact__item">
          <span class="contact__icon">
            <svg width="14" height="16" viewBox="0 0 14 16"><rect x="2" y="1" width="10" height="14" rx="2" fill="none" stroke="#fff" stroke-width="2"/></svg>
          </span>000 - 000 - 000
        </li>
        <li class="contact__item">
          <span class="contact__icon">
            <svg width="16" height="12" viewBox="0 0 16 12"><rect x="1" y="1" width="14" height="10" fill="none" stroke="#fff" stroke-width="1.6"/><path d="M1 1 L8 7 L15 1" fill="none" stroke="#fff" stroke-width="1.6"/></svg>
          </span>name@hcestates-example.com
        </li>
        <li class="contact__item"><span class="contact__icon"></span>video call id here</li>
        <li class="contact__item"><span class="contact__icon"></span>chat app id here</li>
        <li class="contact__item">
          <span class="contact__icon">
            <svg width="16" height="16" viewBox="0 0 16 16"><circle cx="8" cy="8" r="6" fill="none" stroke="#fff" stroke-width="1.6"/><path d="M2 8 H14 M8 2 C5 5 5 11 8 14 C11 11 11 5 8 2" fill="none" stroke="#fff" stroke-width="1.3"/></svg>
          </span>www.hcestates-example.com
        </li>
      </ul>
    </div>
    <div class="address-band">full street address her, city state, zip code</div>
  </section>
</body>
</html>
```